Letterhead, business cards, envelopes
Thornwell Holdings Property Management
Creative Brief
Professional
Dean Pultorak
Real Estate Asset Manager
27816 Brisbane Ave., Los Alamitos Ca 90720
dean@thpropertymgmt.example
www.thpropertymgmt.example
designers choice

```html
<!DOCTYPE html>
<html lang="en">
<head>
<meta charset="utf-8">
<title>Thornwell Holdings Property Management — Stationery</title>
<link rel="stylesheet" href="https://fonts.googleapis.com/css2?family=Open+Sans:wght@400;600;700&display=swap">
<style>
:root{
  --green:#1a7a3c;
  --green-dark:#0f5a2a;
  --black:#1b1b1b;
  --paper:#ffffff;
  --ink:#333333;
  --muted:#8a8a8a;
  --bg:#e9e7e3;
}
*{box-sizing:border-box;margin:0;padding:0}
html,body{width:1200px;height:935px;overflow:hidden}
body{background:var(--bg);font-family:"Open Sans",Arial,sans-serif;color:var(--ink);position:relative}
.sheet{position:absolute;background:var(--paper);box-shadow:0 3px 10px rgba(0,0,0,.25);overflow:hidden}
.wave{position:absolute;left:0;bottom:0;width:100%;display:block}
.brand{display:flex;align-items:center;gap:8px}
.brand-mark{width:30px;height:30px;background:var(--green);flex:none}
.brand-name{font-weight:600;color:var(--green-dark);text-transform:uppercase;line-height:1.1;font-size:12px;letter-spacing:.5px;white-space:nowrap}
.brand-tagline{margin-top:3px;font-size:6px;color:var(--muted);letter-spacing:.6px;text-transform:uppercase;white-space:nowrap}
.contact{position:absolute;display:flex;gap:16px;font-size:6.5px;color:#fff;line-height:1.5;white-space:nowrap}

/* Fax sheet */
.fax{left:45px;top:175px;width:385px;height:730px}
.fax .brand{position:absolute;left:26px;top:24px}
.fax-title{position:absolute;left:26px;top:150px;font-size:30px;font-weight:700;color:var(--black);letter-spacing:1px}
.fax-fields{position:absolute;left:26px;top:210px;width:150px;list-style:none}
.fax-fields li{font-size:9px;font-weight:600;height:34px;border-bottom:1px dotted #aaa;padding-top:18px}
.fax-checks{position:absolute;left:26px;top:360px;display:flex;gap:26px;font-size:9px;white-space:nowrap}
.fax-checks span::before{content:"";display:inline-block;width:8px;height:8px;border:1px solid #888;margin-right:6px;vertical-align:-1px}
.fax-contact{bottom:10px;left:110px}

/* Letterhead */
.letterhead{left:200px;top:85px;width:400px;height:775px}
.letterhead .brand{position:absolute;left:30px;top:32px}
.lh-contact{bottom:14px;left:150px}

/* Envelope */
.envelope{left:505px;top:230px;width:495px;height:310px}
.env-flap{position:absolute;left:0;top:0;width:100%}
.env-flap-mark{position:absolute;left:50%;top:28px;width:22px;height:22px;margin-left:-11px;background:var(--green);border:2px solid #fff}
.envelope .brand{position:absolute;left:30px;top:118px}
.env-address{position:absolute;left:30px;top:160px;font-size:7px;color:var(--ink);white-space:nowrap}
.env-web{position:absolute;right:18px;bottom:8px;font-size:8px;color:#fff;font-weight:600;white-space:nowrap}

/* Business cards */
.card-front{left:855px;top:565px;width:255px;height:140px}
.card-front .brand{position:absolute;left:12px;top:32px}
.card-front .brand-mark{width:22px;height:22px}
.card-front .brand-name{font-size:9px}
.card-person{position:absolute;right:12px;top:8px;text-align:right;white-space:nowrap}
.card-person .name{font-size:9px;font-weight:700;color:var(--black)}
.card-person .role{font-size:6px;color:var(--muted)}
.card-details{position:absolute;left:12px;top:76px;display:flex;gap:12px;font-size:6px;line-height:1.55;color:var(--ink);white-space:nowrap}
.card-back{left:860px;top:720px;width:250px;height:140px;background:var(--black);border-radius:12px}
.card-back-mark{position:absolute;left:50%;top:44px;width:34px;height:34px;margin-left:-17px;background:var(--green);border:2px solid #fff}
.card-back-web{position:absolute;width:100%;top:96px;text-align:center;font-size:7px;color:#fff}
</style>
</head>
<body>

<section class="sheet fax" aria-label="Fax cover sheet">
  <div class="brand">
    <span class="brand-mark"></span>
    <div>
      <div class="brand-name">Thornwell Holdings<br>Property Management</div>
      <div class="brand-tagline">Residential · Commercial · Leasing</div>
    </div>
  </div>
  <h1 class="fax-title">FAX</h1>
  <ul class="fax-fields">
    <li>To :</li><li>Fax :</li><li>Phone :</li><li>Re :</li>
  </ul>
  <div class="fax-checks"><span>Urgent</span><span>For Review</span></div>
  <svg class="wave" viewBox="0 0 385 90" height="90" preserveAspectRatio="none">
    <path d="M0 40 Q190 70 385 10 L385 90 L0 90Z" fill="var(--black)"/>
    <path d="M0 52 Q200 78 385 22 L385 90 L0 90Z" fill="var(--green)"/>
  </svg>
  <div class="contact fax-contact">
    <div>27816 Brisbane Ave.<br>Los Alamitos Ca 90720</div>
    <div>T 714-555-0142<br>F 714-555-0143</div>
    <div>dean@thpropertymgmt.example<br>www.thpropertymgmt.example</div>
  </div>
</section>

<section class="sheet letterhead" aria-label="Letterhead">
  <div class="brand">
    <span class="brand-mark"></span>
    <div>
      <div class="brand-name">Thornwell Holdings<br>Property Management</div>
      <div class="brand-tagline">Residential · Commercial · Leasing</div>
    </div>
  </div>
  <svg class="wave" viewBox="0 0 400 110" height="110" preserveAspectRatio="none">
    <path d="M0 45 Q200 85 400 8 L400 110 L0 110Z" fill="var(--black)"/>
    <path d="M0 58 Q210 92 400 22 L400 110 L0 110Z" fill="var(--green)"/>
  </svg>
  <div class="contact lh-contact">
    <div>27816 Brisbane Ave.<br>Los Alamitos Ca 90720</div>
    <div>T 714-555-0142<br>F 714-555-0143</div>
    <div>dean@thpropertymgmt.example<br>www.thpropertymgmt.example</div>
  </div>
</section>

<section class="sheet envelope" aria-label="Envelope">
  <svg class="env-flap" viewBox="0 0 495 90" height="90" preserveAspectRatio="none">
    <path d="M0 0 H495 V55 Q250 100 0 60Z" fill="var(--black)"/>
  </svg>
  <span class="env-flap-mark"></span>
  <div class="brand">
    <span class="brand-mark"></span>
    <div class="brand-name">Thornwell Holdings<br>Property Management</div>
  </div>
  <p class="env-address">27816 Brisbane Ave., Los Alamitos Ca 90720</p>
  <svg class="wave" viewBox="0 0 495 70" height="70" preserveAspectRatio="none">
    <path d="M0 38 Q260 62 495 8 L495 70 L0 70Z" fill="var(--black)"/>
    <path d="M0 48 Q270 68 495 20 L495 70 L0 70Z" fill="var(--green)"/>
  </svg>
  <p class="env-web">www.thpropertymgmt.example</p>
</section>

<section class="sheet card-front" aria-label="Business card front">
  <div class="card-person">
    <div class="name">Dean Pultorak</div>
    <div class="role">Real Estate Asset Manager</div>
  </div>
  <div class="brand">
    <span class="brand-mark"></span>
    <div class="brand-name">Thornwell Holdings<br>Property Management</div>
  </div>
  <div class="card-details">
    <div>27816 Brisbane Ave.<br>Los Alamitos Ca 90720</div>
    <div>T 714-555-0142<br>C 714-555-0198</div>
    <div>dean@thpropertymgmt.example<br>www.thpropertymgmt.example</div>
  </div>
  <svg class="wave" viewBox="0 0 255 34" height="34" preserveAspectRatio="none">
    <path d="M0 18 Q130 32 255 4 L255 34 L0 34Z" fill="var(--black)"/>
    <path d="M0 24 Q140 36 255 12 L255 34 L0 34Z" fill="var(--green)"/>
  </svg>
</section>

<section class="sheet card-back" aria-label="Business card back">
  <span class="card-back-mark"></span>
  <p class="card-back-web">www.thpropertymgmt.example</p>
</section>

</body>
</html>
```